New website template

Create a new website template based on original logo and company vision.

The ideal outcome would be a PSD containing a home page and a content page.

The domain name is maple-ridge-ventures.co.uk and as you can see currently has a really simple holding page.

The company specialise in commercial property project management and have over 25 years experience in doing so.

Their logo is really simple, it would be nice to keep their site simple, clean, fresh and friendly.

We're planning to use bootstrap to ensure the site works nicely on a mobile device so it would be good if this could be kept in mind when designing the site.

Target Market(s)

commercial property sector.

Industry/Entity Type

It Company

Number of Pages Required

2 page

Font styles to use
Sans Serif

Colors
fece3e

Requirements
Must have
• a home page and a content page.
• bootstrap must be kept in mind when doing the design
• clean, fresh and professional
Should not have
• cartoon graphics.

```html
<!DOCTYPE html>
<html lang="en">
<head>
<meta charset="utf-8">
<title>Maple Ridge Ventures Ltd – Project Management</title>
<link rel="stylesheet" href="https://fonts.googleapis.com/css2?family=Roboto+Condensed:wght@400&family=Oswald:wght@500&family=Roboto:wght@400&family=Lato:wght@400&display=swap">
<style>
  :root {
    --brand-yellow: #fee73e;
    --ink: #111111;
    --ink-soft: #555555;
    --sidebar-bg: #f8f8f8;
    --divider: #c9c9c9;
    --hero-shade: rgba(20, 18, 18, 0.72);
    --footer-bg: #121212;
    --white: #ffffff;
  }
  * { box-sizing: border-box; margin: 0; padding: 0; }
  html, body { width: 1200px; height: 545px; overflow: hidden; }
  body { position: relative; background: var(--white); font-family: "Roboto", Arial, sans-serif; }

  .sidebar {
    position: absolute; left: 0; top: 0; width: 317px; height: 545px;
    background: linear-gradient(180deg, #fbfbfb 0%, var(--sidebar-bg) 60%, #f1f1f1 100%);
    z-index: 2;
  }
  .brand { position: absolute; left: 0; top: 18px; width: 317px; height: 110px; }
  .brand-name {
    position: absolute; right: 15px; top: 58px; white-space: nowrap;
    font-family: "Roboto Condensed", Arial, sans-serif; font-size: 23px; color: var(--ink);
  }
  .brand-tagline {
    position: absolute; left: 128px; top: 88px; white-space: nowrap;
    font-family: "Lato", Arial, sans-serif; font-size: 14px; color: var(--ink-soft);
  }

  .main-nav { position: absolute; left: 0; top: 150px; width: 317px; list-style: none; }
  .main-nav li {
    position: relative; height: 47px; line-height: 47px; text-align: right; padding-right: 17px;
    font-family: "Roboto Condensed", Arial, sans-serif; font-size: 16.5px; color: var(--ink);
    border-bottom: 1px dashed var(--divider);
  }
  .main-nav li.is-active { background: var(--brand-yellow); border-bottom: none; }
  .main-nav li.is-active::after {
    content: ""; position: absolute; right: -14px; top: 0;
    border-top: 23.5px solid transparent; border-bottom: 23.5px solid transparent;
    border-left: 14px solid var(--brand-yellow);
  }

  .contact { position: absolute; right: 19px; top: 409px; list-style: none; font-family: "Lato", Arial, sans-serif; font-size: 12px; color: var(--ink-soft); }
  .contact li { display: flex; justify-content: flex-end; align-items: flex-start; line-height: 17px; margin-bottom: 10px; }
  .contact li svg { margin-left: 12px; margin-top: 2px; flex: none; }
  .contact .address { text-align: right; }

  .social { position: absolute; right: 18px; top: 510px; display: flex; gap: 9px; }
  .social span { width: 32px; height: 32px; border: 1px solid #333; display: block; }

  .hero {
    position: absolute; left: 317px; top: 0; width: 883px; height: 545px;
    background: linear-gradient(180deg, #7a3a2c 0%, #8a4a3a 25%, #9a9188 48%, #6e6a66 70%, #8c8a88 88%, #5a5856 100%);
  }
  .hero-caption {
    position: absolute; left: 117px; top: 151px; width: 678px; height: 154px;
    background: var(--hero-shade); padding: 10px 18px;
  }
  .hero-title { font-family: "Oswald", Arial, sans-serif; font-weight: 500; font-size: 49px; line-height: 1.1; color: var(--white); letter-spacing: 0.6px; }
  .hero-lead { margin-top: 10px; font-size: 18.7px; line-height: 28px; color: var(--white); width: 650px; }

  .site-footer {
    position: absolute; left: 317px; bottom: 0; width: 883px; height: 36px;
    background: var(--footer-bg); color: var(--white); font-size: 12.5px;
    text-align: right; padding-right: 73px; line-height: 36px;
  }
</style>
</head>
<body>
  <aside class="sidebar">
    <div class="brand">
      <div class="brand-name">Maple Ridge Ventures Ltd</div>
      <div class="brand-tagline">Project Management</div>
    </div>

    <ul class="main-nav">
      <li class="is-active">HOME</li>
      <li>ABOUT US</li>
      <li>OUR SERVICES</li>
      <li>PROPERTIES</li>
      <li>CONTACT US</li>
    </ul>

    <ul class="contact">
      <li><span class="address">Maple Ridge Ventures Ltd, PO Box 4812<br>Thornbury, TB7 2QL</span>
        <svg width="12" height="16" viewBox="0 0 12 16"><path d="M6 0C2.7 0 0 2.6 0 5.9 0 10 6 16 6 16s6-6 6-10.1C12 2.6 9.3 0 6 0zm0 8.3a2.4 2.4 0 1 1 0-4.8 2.4 2.4 0 0 1 0 4.8z" fill="#111"/></svg></li>
      <li>info@maple-ridge-ventures.co.uk
        <svg width="14" height="11" viewBox="0 0 14 11"><rect x="0.75" y="0.75" width="12.5" height="9.5" fill="none" stroke="#111" stroke-width="1.5"/><path d="M1 1l6 5 6-5" fill="none" stroke="#111" stroke-width="1.5"/></svg></li>
      <li>0700 900 4123
        <svg width="12" height="12" viewBox="0 0 12 12"><path d="M2.4 0.3l2 2.3-1.2 1.6c.8 1.8 2.2 3.3 4.1 4.1l1.6-1.2 2.3 2-1 2.4C4.8 11.3.7 7.2.3 1.9z" fill="#111"/></svg></li>
    </ul>

    <div class="social" aria-label="Social links">
      <span></span><span></span><span></span><span></span>
    </div>
  </aside>

  <main class="hero" role="img" aria-label="Photograph of a red-brick corner building on a city street with a pedestrian crossing">
    <div class="hero-caption">
      <h1 class="hero-title">It’s all about Attitude</h1>
      <p class="hero-lead">Specialise In Commercial Property Project Management And Have Over 25 Years Experience</p>
    </div>
  </main>

  <footer class="site-footer">© 2014 Maple Ridge Ventures Ltd. All Rights Reserved.</footer>
</body>
</html>
```